Chicken Coop Sign

I would like to make a metal chicken coop sign in the size of 8 x 12 inches. The orientation can be vertical or horizontal.

I would like the designer to use any of these funny phrases and try and create a catchy graphic based on some of the designs that are already in the market.

"The Poultry Palace: Where Every Hen is a Queen"

"The Hen Den: No Foxes Allowed"

"The Eggsecutive Mansion"

"The Cluck Hut: No Fowl Moods Allowed"

"The Cluck and Fluff: Luxury Lodging for Hens"

Target Market(s)

Families that have chicken coops as a hobby in their backyard or farm.

Requirements
Must have
• It must be funny, use one of the provided quotes, have a "vintage" or "rustic" look
Nice to have
Should not have
• Stay away from 4 letter words like "SHIT", "FUCK" or Starred out works like "S**T" and "F**K"

```html
<!DOCTYPE html>
<html lang="en">
<head>
<meta charset="utf-8">
<title>The Hen Den – No Foxes Allowed</title>
<link rel="stylesheet" href="https://fonts.googleapis.com/css2?family=Anton&display=swap">
<style>
  :root {
    --page-bg: #ece6dc;
    --frame: #141414;
    --cream: #f7ebd6;
    --cream-edge: #e6c9a2;
    --red: #e51c23;
    --white: #ffffff;
    --ink: #1a1a1a;
    --shadow-tint: #e2dca6;
    --rule: #e8c8a4;
  }
  * { margin: 0; padding: 0; box-sizing: border-box; }
  html, body {
    width: 1200px;
    height: 1117px;
    overflow: hidden;
    background: var(--page-bg);
  }
  .sign {
    position: absolute;
    left: 253px;
    top: 38px;
    width: 694px;
    height: 1040px;
    background: var(--frame);
    padding: 12px;
  }
  .sign-face {
    position: relative;
    width: 100%;
    height: 100%;
    background: radial-gradient(ellipse at 50% 50%, var(--cream) 62%, var(--cream-edge) 100%);
    overflow: hidden;
  }
  .title-banner {
    position: absolute;
    left: 2px;
    right: 2px;
    top: 2px;
    height: 168px;
    background: var(--red);
    display: flex;
    align-items: center;
    justify-content: center;
    border-bottom: 3px solid var(--white);
  }
  .title-banner h1 {
    font-family: "Anton", "Impact", sans-serif;
    font-weight: 400;
    color: var(--white);
    font-size: 128px;
    line-height: 1;
    letter-spacing: -1px;
    white-space: nowrap;
  }
  .ground-rule {
    position: absolute;
    left: 38px;
    width: 598px;
    top: 455px;
    height: 3px;
    background: var(--rule);
  }
  .photo {
    position: absolute;
    border-radius: 40% 40% 30% 30%;
  }
  .photo-fox {
    left: 126px;
    top: 257px;
    width: 157px;
    height: 242px;
    background: linear-gradient(180deg, #c6753a 0%, #b88a68 55%, #5e5450 100%);
  }
  .photo-hen {
    left: 271px;
    top: 176px;
    width: 237px;
    height: 438px;
    background: linear-gradient(180deg, #c9493a 0%, #b27a55 30%, #c5946e 75%, #d9c2b0 100%);
  }
  .slogan {
    position: absolute;
    left: 0;
    right: 0;
    font-family: "Anton", "Impact", sans-serif;
    font-weight: 400;
    text-align: center;
    font-size: 176px;
    line-height: 1;
    letter-spacing: -2px;
    text-shadow: 6px 6px 0 var(--shadow-tint);
    white-space: nowrap;
  }
  .slogan-no-foxes { top: 615px; color: var(--red); }
  .slogan-allowed { top: 786px; color: var(--ink); }
</style>
</head>
<body>
  <div class="sign">
    <div class="sign-face">
      <header class="title-banner">
        <h1>THE HEN DEN</h1>
      </header>
      <div class="ground-rule"></div>
      <div class="photo photo-fox" role="img" aria-label="Photo of a red fox sitting and smiling"></div>
      <div class="photo photo-hen" role="img" aria-label="Photo of a brown hen standing over a freshly laid egg"></div>
      <p class="slogan slogan-no-foxes">NO FOXES</p>
      <p class="slogan slogan-allowed">ALLOWED</p>
    </div>
  </div>
</body>
</html>
```